Fore Sale sign for my real estate agency

I am a Brisbane - Australia inner western suburbs boutique real estate agent who is needing a for sale sign. We are a small dynamic family agency that needs a for sale sign that will standout and give us a strong presence in the market.

I have attached a logo I like, however I am not fixed on anything and am open to suggestions.

The information on the sign should contain but not necessarily limited to the following information - please appreciate I am very open
1 logo - O'Venny
2 Ph number - 3847 1952
3 web address - ovenny.com.au

Thank you
Gareth O'Venny

```html
<!DOCTYPE html>
<html lang="en">
<head>
<meta charset="utf-8">
<title>O'Venny – For Sale Sign</title>
<link rel="stylesheet" href="https://fonts.googleapis.com/css2?family=Arimo:wght@400;700&display=swap">
<style>
  :root {
    --backdrop: #e4e4e4;
    --sign-orange: #f7941d;
    --sign-black: #231f20;
    --sign-white: #ffffff;
    --band-dark: #5a5a5a;
    --band-light: #9a9a9a;
  }
  html, body {
    margin: 0;
    padding: 0;
    width: 1200px;
    height: 1200px;
    overflow: hidden;
    background: var(--backdrop);
  }
  .canvas {
    position: relative;
    width: 1200px;
    height: 1200px;
  }
  .sale-sign {
    position: absolute;
    left: 78px;
    top: 207px;
    width: 1044px;
    height: 786px;
    display: block;
  }
  .sign-text {
    font-family: "Arimo", Arial, sans-serif;
  }
  .headline { fill: var(--sign-orange); font-weight: 700; }
  .agency-name { fill: var(--sign-black); font-weight: 700; }
  .phone-number { fill: var(--sign-white); font-weight: 700; }
  .web-address { fill: var(--sign-white); font-weight: 400; }
</style>
</head>
<body>
<main class="canvas">
  <svg class="sale-sign" viewBox="65 175 870 655" xmlns="http://www.w3.org/2000/svg" aria-label="O'Venny for sale sign">
    <defs>
      <linearGradient id="band-tone" x1="0" y1="0" x2="1" y2="0">
        <stop offset="0" stop-color="var(--band-dark)"/>
        <stop offset="0.5" stop-color="var(--band-light)"/>
        <stop offset="1" stop-color="var(--band-dark)"/>
      </linearGradient>
    </defs>

    <!-- sign board -->
    <rect class="board" x="65" y="175" width="870" height="655" fill="var(--sign-white)"/>

    <!-- top and bottom bands -->
    <rect class="edge-band edge-band--top" x="65" y="175" width="870" height="30" fill="url(#band-tone)" role="img" aria-label="Black and white checkered border band"/>
    <rect class="edge-band edge-band--bottom" x="65" y="798" width="870" height="32" fill="url(#band-tone)" role="img" aria-label="Black and white checkered border band"/>

    <!-- side panels -->
    <rect class="side-panel side-panel--left" x="65" y="212" width="83" height="578" fill="var(--sign-orange)"/>
    <rect class="side-rule" x="152" y="212" width="7" height="578" fill="var(--sign-black)"/>
    <rect class="side-rule" x="163" y="212" width="3" height="578" fill="var(--sign-black)"/>

    <rect class="side-panel side-panel--right" x="852" y="212" width="83" height="578" fill="var(--sign-orange)"/>
    <rect class="side-rule" x="841" y="212" width="7" height="578" fill="var(--sign-black)"/>
    <rect class="side-rule" x="834" y="212" width="3" height="578" fill="var(--sign-black)"/>

    <!-- headline -->
    <rect class="headline-box" x="172" y="212" width="656" height="84" fill="var(--sign-black)"/>
    <text class="sign-text headline" x="500" y="278" text-anchor="middle" font-size="72" textLength="600" lengthAdjust="spacingAndGlyphs">FOR SALE</text>

    <!-- agency name -->
    <text class="sign-text agency-name" x="500" y="525" text-anchor="middle" font-size="190" textLength="640" lengthAdjust="spacingAndGlyphs">O'Venny</text>

    <!-- contact -->
    <rect class="contact-box" x="172" y="598" width="656" height="192" fill="var(--sign-black)"/>
    <text class="sign-text phone-number" x="500" y="705" text-anchor="middle" font-size="112" textLength="612" lengthAdjust="spacingAndGlyphs">3847 1952</text>
    <text class="sign-text web-address" x="500" y="767" text-anchor="middle" font-size="66" textLength="605" lengthAdjust="spacingAndGlyphs">ovenny.com.au</text>
  </svg>
</main>
</body>
</html>
```